Forensic investigators looking for updated powerpoint design

Louisiana company called Bayline Analytics has an important upcoming meeting and needs a redesigned slideshow template. They are an engineering firm providing evaluation, reporting, and expert witness testimony on a variety of topics to support the litigation and insurance industries. The meeting in question will be held at a conference catering to insurance underwriters.

Target Market(s)

Upcoming tradeshow presentation

Industry/Entity Type

Insurance; TIC (Testing, Inspection, Certification)

Font styles to use
Sans Serif

Colors
0054AA
0677BA
7BADD7
CADEEF
E8F1F8
FFC000
F8CF3A
FAE287
FDF2CF
FEFAEE

Requirements
Must have
• Updated background template with examples of different layouts (bullet list w/ graphic, bullet list without, quote, large central photo, etc.), implementing company logo
Nice to have
• Visual motif that carries through powerpoint designs
Should not have
• No hexagons (old motif of parent company that we're moving away from)

```html
<!DOCTYPE html>
<html lang="en">
<head>
<meta charset="utf-8">
<title>Bayline Analytics – Presentation Template Overview</title>
<link href="https://fonts.googleapis.com/css2?family=Poppins:wght@400;600;700;800&display=swap" rel="stylesheet">
<style>
  :root{
    --navy:#2a2c7c;
    --navy-deep:#212368;
    --yellow:#f6b823;
    --yellow-soft:#fde8a8;
    --ink:#2b2d42;
    --muted:#8d92a3;
    --rule:#e3e5ee;
    --page:#e9eaee;
    --photo:linear-gradient(135deg,#b9c0cc,#7d8799);
  }
  *{margin:0;padding:0;box-sizing:border-box}
  html,body{width:896px;height:1200px;overflow:hidden;background:var(--page);font-family:"Poppins",Arial,sans-serif;color:var(--ink)}
  .deck{display:grid;grid-template-columns:repeat(3,250px);grid-auto-rows:136px;gap:10px 18px;padding:21px 55px}
  .slide{position:relative;background:#fff;overflow:hidden;box-shadow:0 1px 3px rgba(30,32,80,.15)}
  .slide.dark{background:var(--navy)}
  .slide > *{position:absolute}
  .heading{left:12px;top:9px;font-size:8px;font-weight:700;color:var(--navy)}
  .dark .heading{color:#fff}
  .brand{right:10px;top:9px;font-size:5px;font-weight:700;color:var(--navy);display:flex;align-items:center;gap:2px}
  .brand::before{content:"";width:5px;height:5px;background:var(--yellow)}
  .dark .brand{color:#fff}
  .footer{left:12px;right:12px;bottom:6px;height:1px;background:var(--rule)}
  .photo{background:var(--photo)}
  .txt{font-size:3.6px;line-height:1.5;color:var(--muted)}
  .dark .txt{color:#c8cae6}
  .sub{font-size:5px;font-weight:600;color:var(--navy)}
  .dark .sub{color:#fff}
  .dot{width:9px;height:9px;border-radius:50%;background:var(--yellow)}
  .dot.navy{background:var(--navy)}
  .sq{width:10px;height:10px;background:var(--yellow);border-radius:2px}
  .sq.navy{background:var(--navy)}
  .num{font-size:4px;color:#fff;font-weight:700;display:flex;align-items:center;justify-content:center}
  .row{display:flex;align-items:center;gap:4px}
  .col{display:flex;flex-direction:column;gap:5px}
</style>
</head>
<body>
<main class="deck">

  <!-- 1 Title -->
  <section class="slide">
    <div class="brand" style="left:12px;right:auto;top:10px;font-size:6px">Bayline Analytics</div>
    <div style="left:12px;top:36px;font-size:14px;font-weight:800;color:var(--navy);line-height:1.05">Business<br>Marketing</div>
    <div style="left:12px;top:68px;font-size:7px;font-weight:600;color:var(--yellow)">Presentation</div>
    <div class="txt" style="left:12px;top:80px;width:90px">Evaluation, reporting and expert witness services.</div>
    <div class="photo" role="img" aria-label="Team meeting around a laptop" style="left:118px;top:0;width:132px;height:112px"></div>
    <div style="left:0;right:0;bottom:0;height:24px;background:var(--navy)"></div>
    <div style="left:0;bottom:24px;width:118px;height:3px;background:var(--yellow)"></div>
    <div style="left:12px;bottom:9px;font-size:4px;color:#fff">www.baylineanalytics.com</div>
  </section>

  <!-- 2 Table of contents -->
  <section class="slide">
    <div class="heading">Table of Contents</div>
    <div class="brand">Bayline</div>
    <div class="col" style="left:20px;top:32px;gap:9px">
      <div class="row"><div class="dot navy num">1</div><span class="txt">Insert Title Here</span></div>
      <div class="row"><div class="dot navy num">2</div><span class="txt">Insert Title Here</span></div>
      <div class="row"><div class="dot navy num">3</div><span class="txt">Insert Title Here</span></div>
      <div class="row"><div class="dot navy num">4</div><span class="txt">Insert Title Here</span></div>
      <div class="row"><div class="dot navy num">5</div><span class="txt">Insert Title Here</span></div>
    </div>
    <div class="col" style="left:135px;top:32px;gap:9px">
      <div class="row"><div class="dot num">6</div><span class="txt">Insert Title Here</span></div>
      <div class="row"><div class="dot num">7</div><span class="txt">Insert Title Here</span></div>
      <div class="row"><div class="dot num">8</div><span class="txt">Insert Title Here</span></div>
      <div class="row"><div class="dot num">9</div><span class="txt">Insert Title Here</span></div>
      <div class="row"><div class="dot num">10</div><span class="txt">Insert Title Here</span></div>
    </div>
    <div class="footer"></div>
  </section>

  <!-- 3 Photo + two points -->
  <section class="slide">
    <div class="heading">Heading Goes Here</div>
    <div class="brand">Bayline</div>
    <div class="photo" role="img" aria-label="Colleagues discussing at a desk" style="left:12px;top:26px;width:110px;height:92px"></div>
    <div class="col" style="left:132px;top:38px;width:105px;gap:12px">
      <div class="row" style="align-items:flex-start"><div class="sq"></div><div><div class="sub">Your Heading</div><div class="txt">Short text about this point goes here.</div></div></div>
      <div class="row" style="align-items:flex-start"><div class="sq navy"></div><div><div class="sub">Your Heading</div><div class="txt">Short text about this point goes here.</div></div></div>
    </div>
    <div class="footer"></div>
  </section>

  <!-- 4 Photo + icon list -->
  <section class="slide">
    <div class="heading">Heading Goes Here</div>
    <div class="brand">Bayline</div>
    <div class="col" style="left:14px;top:30px;width:95px;gap:9px">
      <div class="row"><div class="dot"></div><div><div class="sub">Your Heading</div><div class="txt">Brief supporting text.</div></div></div>
      <div class="row"><div class="dot"></div><div><div class="sub">Your Heading</div><div class="txt">Brief supporting text.</div></div></div>
      <div class="row"><div class="dot"></div><div><div class="sub">Your Heading</div><div class="txt">Brief supporting text.</div></div></div>
    </div>
    <div class="photo" role="img" aria-label="Engineer reviewing documents" style="left:122px;top:26px;width:116px;height:92px"></div>
    <div class="footer"></div>
  </section>

  <!-- 5 Navy four boxes -->
  <section class="slide dark">
    <div class="heading">Heading Goes Here</div>
    <div class="brand">Bayline</div>
    <svg style="left:0;top:0" width="250" height="136" viewBox="0 0 250 136">
      <g fill="#fff">
        <rect x="40" y="32" width="78" height="38" rx="6"/><rect x="132" y="32" width="78" height="38" rx="6"/>
        <rect x="40" y="80" width="78" height="38" rx="6"/><rect x="132" y="80" width="78" height="38" rx="6"/>
      </g>
      <g fill="#f6b823"><circle cx="118" cy="70" r="7"/><circle cx="132" cy="70" r="7"/><circle cx="118" cy="80" r="7"/><circle cx="132" cy="80" r="7"/></g>
    </svg>
    <div class="txt" style="left:48px;top:40px;width:60px;color:var(--muted)">Add your key point here.</div>
    <div class="txt" style="left:142px;top:40px;width:60px;color:var(--muted)">Add your key point here.</div>
    <div class="txt" style="left:48px;top:96px;width:60px;color:var(--muted)">Add your key point here.</div>
    <div class="txt" style="left:142px;top:96px;width:60px;color:var(--muted)">Add your key point here.</div>
  </section>

  <!-- 6 Half photo -->
  <section class="slide">
    <div class="photo" role="img" aria-label="Business team in a bright office" style="left:0;top:0;width:122px;height:136px"></div>
    <div class="brand">Bayline</div>
    <div style="left:134px;top:28px;font-size:8px;font-weight:700;color:var(--navy)">Heading Here</div>
    <div class="col" style="left:134px;top:44px;width:104px;gap:8px">
      <div class="row"><div class="dot" style="width:5px;height:5px"></div><span class="txt">Point one text here</span></div>
      <div class="row"><div class="dot" style="width:5px;height:5px"></div><span class="txt">Point two text here</span></div>
      <div class="row"><div class="dot" style="width:5px;height:5px"></div><span class="txt">Point three text here</span></div>
      <div class="row"><div class="dot" style="width:5px;height:5px"></div><span class="txt">Point four text here</span></div>
    </div>
  </section>

  <!-- 7 Cycle -->
  <section class="slide">
    <div class="heading">Heading Goes Here</div>
    <div class="brand">Bayline</div>
    <svg style="left:10px;top:24px" width="110" height="104" viewBox="0 0 110 104">
      <circle cx="55" cy="52" r="34" fill="none" stroke="#2a2c7c" stroke-width="1.5" stroke-dasharray="4 3"/>
      <circle cx="55" cy="52" r="14" fill="#2a2c7c"/>
      <circle cx="55" cy="18" r="8" fill="#f6b823"/><circle cx="89" cy="52" r="8" fill="#2a2c7c"/>
      <circle cx="55" cy="86" r="8" fill="#f6b823"/><circle cx="21" cy="52" r="8" fill="#2a2c7c"/>
    </svg>
    <div class="col" style="left:132px;top:34px;width:105px;gap:8px">
      <div><div class="sub">Step One</div><div class="txt">Describe this stage here.</div></div>
      <div><div class="sub">Step Two</div><div class="txt">Describe this stage here.</div></div>
      <div><div class="sub">Step Three</div><div class="txt">Describe this stage here.</div></div>
    </div>
    <div class="footer"></div>
  </section>

  <!-- 8 Bar chart -->
  <section class="slide">
    <div class="heading">Heading Goes Here</div>
    <div class="brand">Bayline</div>
    <svg style="left:14px;top:26px" width="150" height="96" viewBox="0 0 150 96">
      <line x1="0" y1="92" x2="150" y2="92" stroke="#e3e5ee"/>
      <g fill="#2a2c7c"><rect x="6" y="40" width="8" height="52"/><rect x="30" y="22" width="8" height="70"/><rect x="54" y="50" width="8" height="42"/><rect x="78" y="14" width="8" height="78"/><rect x="102" y="34" width="8" height="58"/><rect x="126" y="8" width="8" height="84"/></g>
      <g fill="#f6b823"><rect x="15" y="56" width="8" height="36"/><rect x="39" y="44" width="8" height="48"/><rect x="63" y="30" width="8" height="62"/><rect x="87" y="48" width="8" height="44"/><rect x="111" y="20" width="8" height="72"/><rect x="135" y="40" width="8" height="52"/></g>
    </svg>
    <div class="col" style="left:176px;top:40px;width:64px;gap:8px">
      <div class="row"><div class="sq navy" style="width:6px;height:6px"></div><span class="txt">Series One</span></div>
      <div class="row"><div class="sq" style="width:6px;height:6px"></div><span class="txt">Series Two</span></div>
      <div class="txt">Summarize the data trend here.</div>
    </div>
    <div class="footer"></div>
  </section>

  <!-- 9 Text + boxes -->
  <section class="slide">
    <div class="heading">Heading Goes Here</div>
    <div class="brand">Bayline</div>
    <div class="col" style="left:14px;top:32px;width:96px;gap:8px">
      <div><div class="sub">Your Heading</div><div class="txt">Supporting text for this section goes here.</div></div>
      <div><div class="sub">Your Heading</div><div class="txt">Supporting text for this section goes here.</div></div>
    </div>
    <div style="left:122px;top:30px;width:56px;height:40px;background:var(--yellow);border-radius:4px"></div>
    <div style="left:182px;top:30px;width:56px;height:40px;background:var(--navy);border-radius:4px"></div>
    <div style="left:122px;top:76px;width:56px;height:40px;background:var(--navy);border-radius:4px"></div>
    <div style="left:182px;top:76px;width:56px;height:40px;background:var(--yellow);border-radius:4px"></div>
    <div class="footer"></div>
  </section>

  <!-- 10 Two photos -->
  <section class="slide">
    <div class="heading">Heading Goes Here</div>
    <div class="brand">Bayline</div>
    <div class="photo" role="img" aria-label="Inspector on site" style="left:12px;top:26px;width:108px;height:62px"></div>
    <div class="photo" role="img" aria-label="Meeting room discussion" style="left:130px;top:26px;width:108px;height:62px"></div>
    <div style="left:12px;top:94px;width:108px"><div class="sub">Your Heading</div><div class="txt">Short caption for this photo.</div></div>
    <div style="left:130px;top:94px;width:108px"><div class="sub">Your Heading</div><div class="txt">Short caption for this photo.</div></div>
  </section>

  <!-- 11 Three cards -->
  <section class="slide">
    <div class="heading">Heading Goes Here</div>
    <div class="brand">Bayline</div>
    <div class="photo" role="img" aria-label="Office worker" style="left:12px;top:28px;width:70px;height:48px"></div>
    <div class="photo" role="img" aria-label="Handshake in office" style="left:90px;top:28px;width:70px;height:48px"></div>
    <div class="photo" role="img" aria-label="Analyst at computer" style="left:168px;top:28px;width:70px;height:48px"></div>
    <div style="left:12px;top:82px;width:70px"><div class="sub">Title</div><div class="txt">Brief card text here.</div></div>
    <div style="left:90px;top:82px;width:70px"><div class="sub">Title</div><div class="txt">Brief card text here.</div></div>
    <div style="left:168px;top:82px;width:70px"><div class="sub">Title</div><div class="txt">Brief card text here.</div></div>
    <div class="footer"></div>
  </section>

  <!-- 12 Icon list -->
  <section class="slide">
    <div class="heading">Heading Goes Here</div>
    <div class="brand">Bayline</div>
    <div class="col" style="left:14px;top:32px;gap:10px">
      <div class="row"><div class="sq"></div><span class="txt">Number of Products</span></div>
      <div class="row"><div class="sq navy"></div><span class="txt">Number of Products</span></div>
      <div class="row"><div class="sq"></div><span class="txt">Number of Products</span></div>
    </div>
    <div class="col" style="left:130px;top:32px;gap:10px">
      <div class="row"><div class="sq navy"></div><span class="txt">Number of Products</span></div>
      <div class="row"><div class="sq"></div><span class="txt">Number of Products</span></div>
      <div class="row"><div class="sq navy"></div><span class="txt">Number of Products</span></div>
    </div>
    <div class="footer"></div>
  </section>

  <!-- 13 Photo row -->
  <section class="slide">
    <div class="heading">Heading Goes Here</div>
    <div class="brand">Bayline</div>
    <div class="photo" role="img" aria-label="Team at conference table" style="left:12px;top:26px;width:140px;height:60px"></div>
    <div class="photo" role="img" aria-label="Engineer portrait in office" style="left:160px;top:26px;width:78px;height:60px"></div>
    <div class="txt" style="left:12px;top:94px;width:140px">Place a short description of the image content and its context here.</div>
    <div class="footer"></div>
  </section>

  <!-- 14 Ring diagram -->
  <section class="slide">
    <div class="heading">Heading Goes Here</div>
    <div class="brand">Bayline</div>
    <svg style="left:85px;top:26px" width="80" height="80" viewBox="0 0 80 80">
      <g fill="none" stroke-width="14">
        <path d="M40 8 A32 32 0 0 1 72 40" stroke="#f6b823"/>
        <path d="M72 40 A32 32 0 0 1 40 72" stroke="#2a2c7c"/>
        <path d="M40 72 A32 32 0 0 1 8 40" stroke="#f6b823"/>
        <path d="M8 40 A32 32 0 0 1 40 8" stroke="#2a2c7c"/>
      </g>
    </svg>
    <div style="left:105px;top:62px;width:40px;text-align:center;font-size:4px;font-weight:700;color:var(--navy)">Title Here</div>
    <div class="col" style="left:12px;top:36px;width:66px;gap:14px">
      <div class="txt">Text for segment one.</div><div class="txt">Text for segment four.</div>
    </div>
    <div class="col" style="left:174px;top:36px;width:66px;gap:14px">
      <div class="txt">Text for segment two.</div><div class="txt">Text for segment three.</div>
    </div>
    <div class="footer"></div>
  </section>

  <!-- 15 Numbered list -->
  <section class="slide">
    <div class="heading">Heading Goes Here</div>
    <div class="brand">Bayline</div>
    <div class="col" style="left:16px;top:28px;gap:7px">
      <div class="row"><div class="dot num">1</div><span class="txt">Add Text Title Of Product Here</span></div>
      <div class="row"><div class="dot navy num">2</div><span class="txt">Add Text Title Of Product Here</span></div>
      <div class="row"><div class="dot num">3</div><span class="txt">Add Text Title Of Product Here</span></div>
      <div class="row"><div class="dot navy num">4</div><span class="txt">Add Text Title Of Product Here</span></div>
      <div class="row"><div class="dot num">5</div><span class="txt">Add Text Title Of Product Here</span></div>
    </div>
    <div class="footer"></div>
  </section>

  <!-- 16 Heading + photo -->
  <section class="slide">
    <div class="photo" role="img" aria-label="Desk with laptop and charts" style="left:0;top:0;width:112px;height:136px"></div>
    <div class="brand">Bayline</div>
    <div style="left:124px;top:34px;font-size:10px;font-weight:800;line-height:1.1;color:var(--yellow)">Heading<br><span style="color:var(--navy)">Text Goes Here</span></div>
    <div class="txt" style="left:124px;top:64px;width:112px">Use this layout for a key message supported by a single strong photograph.</div>
    <div style="left:124px;top:90px;width:30px;height:3px;background:var(--yellow)"></div>
  </section>

  <!-- 17 Section divider -->
  <section class="slide dark">
    <div style="left:22px;top:26px;font-size:48px;font-weight:800;color:var(--yellow);line-height:1">01</div>
    <div style="left:110px;top:44px;font-size:13px;font-weight:700;color:#fff">Part One</div>
    <div class="txt" style="left:110px;top:64px;width:110px">Short introduction to this section.</div>
    <div class="brand" style="right:auto;left:110px;top:auto;bottom:12px;font-size:6px">Bayline Analytics</div>
  </section>

  <!-- 18 Icon grid -->
  <section class="slide">
    <div class="heading">Heading Goes Here</div>
    <div class="brand">Bayline</div>
    <div style="left:16px;top:30px;display:grid;grid-template-columns:repeat(3,70px);gap:14px 8px">
      <div class="row"><div class="sq"></div><span class="txt">Your Title</span></div>
      <div class="row"><div class="sq"></div><span class="txt">Your Title</span></div>
      <div class="row"><div class="sq"></div><span class="txt">Your Title</span></div>
      <div class="row"><div class="sq navy"></div><span class="txt">Your Title</span></div>
      <div class="row"><div class="sq navy"></div><span class="txt">Your Title</span></div>
      <div class="row"><div class="sq navy"></div><span class="txt">Your Title</span></div>
    </div>
    <div class="txt" style="left:16px;top:96px;width:220px">Add a short summary line below the icon grid.</div>
    <div class="footer"></div>
  </section>

  <!-- 19 Two columns -->
  <section class="slide">
    <div class="heading">Heading Goes Here</div>
    <div class="brand">Bayline</div>
    <div style="left:12px;top:28px;width:108px;height:96px;border:1px solid var(--rule)"></div>
    <div style="left:130px;top:28px;width:108px;height:96px;border:1px solid var(--rule)"></div>
    <div style="left:12px;top:28px;width:60px;height:10px;background:var(--yellow);font-size:4px;font-weight:700;color:var(--navy);padding:3px 5px">Your Title Here</div>
    <div style="left:130px;top:28px;width:60px;height:10px;background:var(--navy);font-size:4px;font-weight:700;color:#fff;padding:3px 5px">Your Title Here</div>
    <div class="txt" style="left:18px;top:46px;width:96px">Describe the first option in a few short lines of text here.</div>
    <div class="txt" style="left:136px;top:46px;width:96px">Describe the second option in a few short lines of text here.</div>
  </section>

  <!-- 20 Circle + list -->
  <section class="slide">
    <div class="heading">Heading Goes Here</div>
    <div class="brand">Bayline</div>
    <div style="left:18px;top:30px;width:80px;height:80px;border-radius:50%;background:var(--yellow);border:5px solid var(--navy)"></div>
    <div style="left:30px;top:62px;width:56px;text-align:center;font-size:6px;font-weight:700;color:var(--navy)">Your Title</div>
    <div class="col" style="left:114px;top:30px;gap:8px">
      <div class="row"><div class="dot navy"></div><span class="txt">Milestone text goes here</span></div>
      <div class="row"><div class="dot navy"></div><span class="txt">Milestone text goes here</span></div>
      <div class="row"><div class="dot navy"></div><span class="txt">Milestone text goes here</span></div>
      <div class="row"><div class="dot navy"></div><span class="txt">Milestone text goes here</span></div>
    </div>
    <div class="footer"></div>
  </section>

  <!-- 21 Timeline -->
  <section class="slide">
    <div class="heading">Heading Goes Here</div>
    <div class="brand">Bayline</div>
    <svg style="left:0;top:50px" width="250" height="30" viewBox="0 0 250 30">
      <rect x="12" y="13" width="226" height="4" fill="#2a2c7c"/>
      <g fill="#f6b823" stroke="#fff" stroke-width="2"><circle cx="30" cy="15" r="9"/><circle cx="77" cy="15" r="9"/><circle cx="125" cy="15" r="9"/><circle cx="173" cy="15" r="9"/><circle cx="220" cy="15" r="9"/></g>
    </svg>
    <div class="txt" style="left:12px;top:86px;width:40px;text-align:center">Stage one</div>
    <div class="txt" style="left:57px;top:36px;width:40px;text-align:center">Stage two</div>
    <div class="txt" style="left:105px;top:86px;width:40px;text-align:center">Stage three</div>
    <div class="txt" style="left:153px;top:36px;width:40px;text-align:center">Stage four</div>
    <div class="txt" style="left:200px;top:86px;width:40px;text-align:center">Stage five</div>
    <div class="footer"></div>
  </section>

  <!-- 22 Devices -->
  <section class="slide">
    <div class="heading">Heading Goes Here</div>
    <div class="brand">Bayline</div>
    <div class="col" style="left:14px;top:34px;width:76px;gap:8px">
      <div><div class="sub">Your Title</div><div class="txt">Feature description text.</div></div>
      <div><div class="sub">Your Title</div><div class="txt">Feature description text.</div></div>
    </div>
    <div role="img" aria-label="Smartphone screen showing the app" style="left:104px;top:30px;width:38px;height:72px;border-radius:5px;background:linear-gradient(160deg,#d5d9e2,#9aa2b3)"></div>
    <div role="img" aria-label="Smartphone screen showing the app" style="left:150px;top:22px;width:38px;height:72px;border-radius:5px;background:linear-gradient(160deg,#d5d9e2,#9aa2b3)"></div>
    <div role="img" aria-label="Smartphone screen showing the app" style="left:196px;top:34px;width:38px;height:72px;border-radius:5px;background:linear-gradient(160deg,#d5d9e2,#9aa2b3)"></div>
    <div class="footer"></div>
  </section>

  <!-- 23 Team -->
  <section class="slide">
    <div class="heading">Heading Goes Here</div>
    <div class="brand">Bayline</div>
    <div class="photo" role="img" aria-label="Team member portrait" style="left:34px;top:30px;width:44px;height:44px;border-radius:50%;border:2px solid var(--yellow)"></div>
    <div class="photo" role="img" aria-label="Team member portrait" style="left:103px;top:30px;width:44px;height:44px;border-radius:50%;border:2px solid var(--yellow)"></div>
    <div class="photo" role="img" aria-label="Team member portrait" style="left:172px;top:30px;width:44px;height:44px;border-radius:50%;border:2px solid var(--yellow)"></div>
    <div style="left:24px;top:80px;width:64px;height:10px;background:var(--navy);color:#fff;font-size:4px;text-align:center;padding-top:2px">Name Here</div>
    <div style="left:93px;top:80px;width:64px;height:10px;background:var(--navy);color:#fff;font-size:4px;text-align:center;padding-top:2px">Name Here</div>
    <div style="left:162px;top:80px;width:64px;height:10px;background:var(--navy);color:#fff;font-size:4px;text-align:center;padding-top:2px">Name Here</div>
    <div class="txt" style="left:24px;top:94px;width:64px;text-align:center">Job Position</div>
    <div class="txt" style="left:93px;top:94px;width:64px;text-align:center">Job Position</div>
    <div class="txt" style="left:162px;top:94px;width:64px;text-align:center">Job Position</div>
    <div class="footer"></div>
  </section>

  <!-- 24 Thank you -->
  <section class="slide dark">
    <div class="brand" style="right:auto;left:16px;top:38px;font-size:9px;gap:4px">Bayline Analytics</div>
    <div class="txt" style="left:16px;top:56px;width:100px">Evaluation · Reporting · Expert Testimony</div>
    <div style="left:130px;top:0;width:120px;height:136px;background:var(--navy-deep)"></div>
    <div style="left:142px;top:34px;font-size:15px;font-weight:800;color:#fff">Thank You</div>
    <div class="col" style="left:142px;top:62px;gap:5px">
      <div class="row"><div class="dot" style="width:5px;height:5px"></div><span class="txt">+1 (504) 555-0142</span></div>
      <div class="row"><div class="dot" style="width:5px;height:5px"></div><span class="txt">hello@baylineanalytics.com</span></div>
      <div class="row"><div class="dot" style="width:5px;height:5px"></div><span class="txt">www.baylineanalytics.com</span></div>
    </div>
    <div style="left:0;bottom:0;width:130px;height:4px;background:var(--yellow)"></div>
  </section>

</main>
</body>
</html>
```